A very simple 3-4 page website, wine consluting
A comprehensive and clear design brief is included
Beverages
www.veLumaconsulting.example
see brief
left side
JPG company logo, many formats available
EPS company logo, many formats available
Website Brief
my photo, not required
For Gavin
for Gavin

```html
<!DOCTYPE html>
<html lang="en">
<head>
<meta charset="utf-8">
<title>veLuma consulting</title>
<link rel="stylesheet" href="https://fonts.googleapis.com/css2?family=Open+Sans:wght@400;600&family=Quicksand:wght@400;500;700&display=swap">
<style>
  :root {
    --page-bg: #1b1b1b;
    --spot: rgba(255,255,255,0.32);
    --wine: #8e1f24;
    --wine-dark: #4b1517;
    --wine-band: #5a1a1c;
    --nav-bg: #343434;
    --nav-text: #d0d0d0;
    --quote-text: #bdbdbd;
    --footer-text: #e4d6d6;
    --tag-text: #9a9a9a;
  }
  * { margin: 0; padding: 0; box-sizing: border-box; }
  html, body { width: 1200px; height: 901px; overflow: hidden; }
  body {
    position: relative;
    background:
      radial-gradient(ellipse 330px 300px at 175px 70px, var(--spot), rgba(255,255,255,0.06) 60%, transparent 100%),
      var(--page-bg);
    font-family: "Open Sans", Arial, sans-serif;
  }
  .brand {
    position: absolute;
    left: 70px;
    top: 78px;
    display: flex;
    align-items: center;
    gap: 18px;
  }
  .brand-dot {
    width: 34px; height: 34px;
    border-radius: 50%;
    background: var(--wine);
  }
  .brand-name {
    font-family: "Quicksand", Arial, sans-serif;
    font-weight: 700;
    font-size: 62px;
    line-height: 1;
    color: var(--wine);
    letter-spacing: 1px;
  }
  .brand-tagline {
    position: absolute;
    left: 282px;
    top: 200px;
    font-size: 13px;
    color: var(--tag-text);
    letter-spacing: 0.5px;
  }
  .header-rule {
    position: absolute;
    left: 525px;
    top: 203px;
    width: 675px;
    height: 14px;
    background: var(--wine-band);
    border-radius: 7px 0 0 7px;
  }
  .main-nav {
    position: absolute;
    left: 56px;
    top: 321px;
    display: flex;
    flex-direction: column;
    gap: 22px;
  }
  .nav-link {
    display: flex;
    align-items: center;
    width: 173px;
    height: 73px;
    padding-left: 16px;
    background: var(--nav-bg);
    color: var(--nav-text);
    font-size: 24px;
    text-decoration: none;
  }
  .intro-quote {
    position: absolute;
    left: 370px;
    top: 322px;
    width: 650px;
    text-align: center;
    font-family: "Quicksand", Arial, sans-serif;
    font-style: italic;
    font-weight: 400;
    font-size: 30px;
    line-height: 41px;
    letter-spacing: 1px;
    color: var(--quote-text);
  }
  .site-footer {
    position: absolute;
    left: 19px;
    top: 798px;
    width: 1169px;
    height: 36px;
    background: var(--wine-dark);
    border-radius: 10px;
    color: var(--footer-text);
    font-size: 16px;
  }
  .site-footer span { position: absolute; top: 7px; }
  .footer-email { left: 207px; }
  .footer-phone { left: 499px; }
  .footer-skype { left: 755px; }
</style>
</head>
<body>
  <header>
    <div class="brand">
      <span class="brand-dot"></span>
      <span class="brand-name">veLuma consulting</span>
    </div>
    <p class="brand-tagline">your China wine market insider</p>
    <div class="header-rule"></div>
  </header>

  <nav class="main-nav">
    <a class="nav-link" href="#who">Who we are</a>
    <a class="nav-link" href="#what">What we do</a>
    <a class="nav-link" href="#contact">Contact us</a>
  </nav>

  <blockquote class="intro-quote">“In order to succeed in this uniquely challenging market, you need someone intimately familiar with the market who can assist you in achieving your goals. veLuma consulting, with over nine years of experience in the market, is your China wine market insider”</blockquote>

  <footer class="site-footer">
    <span class="footer-email">info@veLumaconsulting.example</span>
    <span class="footer-phone">Tel: +852 5550 2046</span>
    <span class="footer-skype">Skype: veluma.consulting</span>
  </footer>
</body>
</html>
```